Regenerative Medicine Brochure

I want a clean modern bi-fold or tri-fold brochure. We offer non-surgical joint repair for knees, shoulders, and hips. We have many services available including regenerative medicine including stem cell allograft, palatelet rich plasma, prolotherapy, triggerpoint injection, chiropractic and rehab therapies. We are a modern multidisciplinary clinic in coastal California. My logo is already complete and is a vibrant green color. I prefer lots of white space with some areas for service description and what conditions may benefit from the services. Design should convey modern treatments, upscale office and practice, and our target audience is older adults who want to maintain an active pain-free lifestyle.

Target Market(s)

Sports injuries, athletes, seniors who are active, knee pain, shoulder pain, arthritis.

Industry/Entity Type

Alternative Medicine

Font styles to use
Serif

Colors
9bcb3c

Requirements
Must have
• Small white space where we can write date, time, location of next event/class. Colors in brochure to coordinate with logo colors provided.

```html
<!DOCTYPE html>
<html lang="en">
<head>
<meta charset="utf-8">
<title>Regenerative Medicine Brochure – Coastline Spine &amp; Joint</title>
<link rel="stylesheet" href="https://fonts.googleapis.com/css2?family=Noticia+Text:ital,wght@0,400;0,700;1,400;1,700&family=PT+Serif:ital,wght@0,400;0,700;1,400;1,700&display=swap">
<style>
  :root {
    --green: #4cb848;
    --ink: #1c1c1c;
    --paper: #ffffff;
    --quote-bg: #eef0ee;
    --hero-deep: #5a9ccf;
    --hero-light: #d9ecf7;
  }
  * { margin: 0; padding: 0; box-sizing: border-box; }
  html, body { width: 1200px; height: 848px; overflow: hidden; background: var(--paper); }
  body { font-family: "PT Serif", Georgia, serif; color: var(--ink); position: relative; }

  .hero { position: absolute; left: 0; top: 0; width: 1200px; height: 202px; overflow: hidden; }
  .hero-photo {
    position: absolute; inset: 0;
    background:
      radial-gradient(ellipse at 62% 45%, rgba(255,255,255,.85) 0%, rgba(220,232,240,.6) 25%, rgba(0,0,0,0) 55%),
      radial-gradient(ellipse at 90% 60%, #e4c2a6 0%, #f3efec 30%, rgba(0,0,0,0) 55%),
      linear-gradient(90deg, var(--hero-deep) 0%, #8fc2e6 30%, var(--hero-light) 55%, #eef3f6 100%);
  }
  .hero-intro {
    position: absolute; left: 20px; top: 22px; width: 360px;
    font-family: "Noticia Text", Georgia, serif;
    font-weight: 700; font-size: 13.2px; line-height: 18.6px; text-align: justify;
    color: #111;
  }

  .band {
    position: absolute; left: 0; top: 202px; width: 1200px; height: 77px;
    background: var(--green); color: var(--paper);
    display: grid; grid-template-columns: 398px 398px 404px; align-items: center;
  }
  .band-title { text-align: center; font-weight: 400; font-size: 14px; line-height: 17px; letter-spacing: .4px; }
  .band-title em { display: block; font-weight: 700; font-style: italic; font-size: 14.5px; }

  .column {
    position: absolute; top: 293px; height: 540px;
    display: flex; flex-direction: column;
    font-size: 12px; line-height: 18.4px; text-align: justify;
  }
  .column p { margin-bottom: 7px; }
  .col-what { left: 19px; width: 368px; }
  .col-how { left: 422px; width: 356px; }
  .col-expect { left: 815px; width: 366px; }

  .areas-heading { font-weight: 700; font-size: 14px; line-height: 19px; text-align: left; margin-top: 2px; }
  .areas { list-style: none; display: grid; grid-template-columns: 99px 95px 95px; margin: -2px 0 8px 63px; line-height: 17.5px; font-size: 12.4px; }
  .areas li, .steps li { position: relative; }
  .areas li { padding-left: 13px; }
  .areas li::before, .steps li::before {
    content: ""; position: absolute; left: 0; width: 7px; height: 7px; background: var(--green);
  }
  .areas li::before { top: 6px; }

  .pull-quote {
    margin-top: auto; flex-shrink: 0;
    background: var(--quote-bg); padding: 6px 10px 10px;
    font-family: "Noticia Text", Georgia, serif;
    color: var(--green); font-weight: 700; font-style: italic;
    font-size: 18px; line-height: 21.3px; text-align: justify; letter-spacing: .4px;
  }

  .steps { list-style: none; }
  .steps li { padding-left: 18px; margin-bottom: 8px; }
  .steps li::before { left: 0; top: 5px; }

  .event { margin-top: auto; padding-bottom: 22px; font-weight: 700; font-style: italic; font-size: 12.6px; text-align: left; }
  .event p { margin-bottom: 0; }
  .event-fields { display: grid; grid-template-columns: 110px 100px 1fr; margin-top: 16px; }
</style>
</head>
<body>
  <header class="hero">
    <div class="hero-photo" role="img" aria-label="Photo of a clinician pointing at a chest X-ray film held up to the light"></div>
    <p class="hero-intro">For joint arthritis and muscle pain and injuries, the team at Coastline Spine &amp; Joint offers minimally invasive regenerative medicine techniques to help you recover from chronic pain. Located in Harbor Point, California, the medical team utilizes advanced restorative techniques to support the natural healing of injured joints and soft tissues without the need for surgery.</p>
  </header>

  <div class="band">
    <h2 class="band-title"><em>WHAT IS</em>REGENERATIVE MEDICINE ?</h2>
    <h2 class="band-title"><em>HOW DOES</em>REGENERATIVE MEDICINE WORK?</h2>
    <h2 class="band-title"><em>WHAT CAN I EXPECT FROM</em>REGENERATIVE MEDICINE TREATMENTS?</h2>
  </div>

  <section class="column col-what">
    <p>Regenerative medicine is a form of biotechnology that involves injecting regenerative medicine products into injured tissues to help your body repair damage. Regenerative medicine uses tissue engineering techniques to repair muscles, ligaments, cartilage, and tendons damaged by injuries, overuse, and osteoarthritis. The medical providers at Coastline Spine &amp; Joint select from a variety of available treatments and products. These include amniotic allografts, hyaluronic acid, regenerative cells, and cytokines which are powerful growth factors that may help regenerate your own body’s tissues.</p>
    <p>After you’re injection with the amniotic allograft serum, the growth factors trigger repair at the site of injection. Over the course of the next several weeks, cells grow and multiply forming new tissue.</p>
    <h3 class="areas-heading">Regenerative medicine may be used in the following areas:</h3>
    <ul class="areas">
      <li>Shoulder</li><li>Elbow</li><li>Wrist</li>
      <li>Hip</li><li>Knee</li><li>Ankle</li>
    </ul>
    <p>There are many additional types of bone and soft tissue problems, including arthritis, that these injections may benefit.</p>
    <p>With regenerative medicine and amniotic allograft treatments, the team supports the natural healing abilities of your body without the need for drugs or surgical repair and painful recovery. However, not all forms of regenerative medicine are equal. At Coastline Spine &amp; Joint, the team only works with the best regenerative medicine labs to ensure that the right kind of products are selected and that they are of the best quality and highest safety.</p>
  </section>

  <section class="column col-how">
    <p>The team uses lab-grade products that are sterilized and processed to inject into the injured area. Once injected, it is thought that these powerful products differentiate into a variety of tissues to trigger your own body to repair damaged tissues. This damage may involve minor tears in muscles, ligaments, and tendons, or cartilage and meniscus breakdown in joints.</p>
    <p>Regenerative medicine products contain the basic building blocks of the body tissues — including proteins, amino acids, and cytokines — responsible for healing and tissue growth. They also provide anti-inflammatory benefits by promoting repair of tissues affected by inflammation.</p>
    <p>While some inflammation is normal and has a benefit to healing injuries, long-term inflammation causes pain, swelling, and further damage to tissues. When you experience too much inflammation, it does more harm than good. Instead of constantly relying on anti-inflammatory medications, regenerative products may be able to correct the problem at the source and reduce the production of natural inflammatory chemicals so you can heal.</p>
    <blockquote class="pull-quote">Regenerative medicine treatment products contain the basic building blocks of the body tissues — including proteins, amino acids, and cytokines — responsible for healing and tissue growth.</blockquote>
  </section>

  <section class="column col-expect">
    <p>During your visit, the team begins with a consultation and physical exam to determine if you’re a candidate for regenerative medicine. They ask about your symptoms, condition, overall health, and lifestyle. If you’re a candidate, the team then explains the procedure and what to expect both during and afterward.</p>
    <p>For the procedure:</p>
    <ul class="steps">
      <li>The team first cleans your skin and applies a topical numbing cream to your skin, if needed.</li>
      <li>The team injects regenerative products into the treatment area. You may feel a slight pinch or burning sensation during the injection. The injection takes less than five minutes and you can return to your usual activities the same day. Mild soreness at the injection site is possible for two to three days.</li>
      <li>Over the coming weeks and months, the injected products help repair damaged tissues at the treatment site. Most people notice results after two months.</li>
      <li>Follow-up care may be recommended based on your condition and initial results.</li>
      <li>The team has seen dramatic results with regenerative medicine treatments, however, individual results can vary. Speak to the team to see if regenerative medicine is right for you.</li>
    </ul>
    <aside class="event">
      <p>Next class/event schedule:</p>
      <div class="event-fields"><span>Date:</span><span>Time:</span><span>Location:</span></div>
    </aside>
  </section>
</body>
</html>
```